Dental equipment company needs Black Friday email design

We are launching a black Friday/Cyber Monday sale and need a great email design to send (via Mailchimp) to our prospects. We want a bold design that hopefully has some movement to some elements. Must be able to import HTML into Mailchimp. Want to have project done by 11//22 for an 11/23 launch.

Target Market(s)

Dentists.

Requirements
Must have
• Must use our colors:
Orange - #ff6319
Teal - #56b1bf
Lt. Teal - #aed9da
Blue: #38394B
Our logo
picture of our sensor and logo (uploaded)
details of our offer.

We sell a dental x-ray sensor called VANTA. we sell it through a subscription service that costs $1,999 to sign up (one time fee) and then just $139/mo. For Black Friday/Cyber Monday we are doing a BOGO (Buy one, get one) for 50% off the sign up fee on the 2nd one (see attached image describing the sale for guidance please do not use that image, it's just there to provide clarity on the black friday/cyber monday offer ). Also, please make sure it includes that the offer expires Dec 1st 2020.

Any links on email should land on: https://www.pelkoradiant.com/sensor-shop/
Nice to have
• We would like to see some sort of movement in the email
We have some elements we use to describe our offering that could be included:
1) VANTA is GUARANTEED to work seamlessly in all major imaging software applications, including Morvex 9/10/11, Talden QRP, Brivolane, Quorin TelaPix, Novrida, Harbinview/Whitcombe Imaging, Stelvar Kobinex and more!

2) No Risk….try us worry free for 30 days or your money back!

3) Lifetime no-deductible warranty, support and software upgrades for PELKO Circle members

```html
<!DOCTYPE html>
<html lang="en">
<head>
<meta charset="utf-8">
<title>PELKO Radiant – Subscribe Offer</title>
<link href="https://fonts.googleapis.com/css2?family=IBM+Plex+Sans:wght@400;700&family=Prata&display=swap" rel="stylesheet">
<style>
  :root {
    --orange: #ff6319;
    --teal: #56b1bf;
    --lt-teal: #aed9da;
    --blue: #38394b;
    --navy: #1c2546;
    --header-bg: #eceef2;
    --card-bg: #dcf2f3;
    --icon-bg: #cfe0e3;
    --body-text: #2a2f45;
    --white: #ffffff;
  }
  * { margin: 0; padding: 0; box-sizing: border-box; }
  html, body { width: 1200px; height: 3532px; overflow: hidden; }
  body { font-family: "IBM Plex Sans", sans-serif; background: var(--white); position: relative; }

  .header { position: absolute; left: 0; top: 0; width: 1200px; height: 1030px; background: var(--header-bg); }
  .brand { position: absolute; left: 44px; top: 60px; display: flex; flex-direction: column; line-height: 1; }
  .brand-name { font-weight: 700; font-size: 96px; color: var(--navy); letter-spacing: -2px; }
  .brand-sub { font-weight: 700; font-size: 46px; color: var(--navy); letter-spacing: 4px; margin-top: 6px; }
  .contact { position: absolute; left: 576px; top: 56px; display: flex; align-items: center; gap: 22px; }
  .contact-label { font-size: 38px; color: var(--navy); letter-spacing: 1px; }
  .contact-number { font-family: "Prata", serif; font-size: 64px; color: var(--navy); line-height: 1.1; }
  .sensor-visual { position: absolute; left: 0; top: 250px; width: 1200px; height: 780px;
    background: radial-gradient(ellipse 460px 340px at 670px 360px, #3a3d5e 0%, #4a4d6c 55%, rgba(236,238,242,0) 100%); }

  .subscribe { position: absolute; left: 0; top: 1030px; width: 1200px; height: 566px; background: var(--blue); text-align: center; }
  .section-title { font-weight: 700; font-size: 56px; letter-spacing: 2px; padding-top: 68px; color: var(--white); }
  .rule { width: 104px; height: 5px; margin: 18px auto 0; background: var(--white); }
  .price { position: absolute; top: 236px; height: 220px; border: 3px solid var(--orange); border-radius: 10px; }
  .price-one { left: 130px; width: 460px; }
  .price-two { left: 664px; width: 402px; }
  .price-amount { font-family: "Prata", serif; font-size: 128px; color: var(--orange); line-height: 1; margin-top: 26px; }
  .price-tag { position: absolute; left: 50%; transform: translateX(-50%); bottom: -40px; background: var(--orange); color: var(--white);
    font-size: 44px; padding: 2px 22px; border-radius: 10px; white-space: nowrap; }

  .promo { position: absolute; left: 0; top: 1596px; width: 1200px; height: 376px; background: var(--teal); text-align: center; color: var(--white); }
  .promo-headline { font-family: "Prata", serif; font-size: 92px; margin-top: 46px; line-height: 1.2; }
  .promo-expiry { display: inline-block; margin-top: 22px; border: 2px solid var(--white); border-radius: 12px; padding: 16px 38px; font-size: 38px; }

  .offers { position: absolute; left: 0; top: 1972px; width: 1200px; height: 1432px; background: var(--lt-teal); }
  .offers .section-title { color: var(--navy); padding-top: 78px; text-align: center; }
  .offers .rule { background: var(--orange); width: 120px; }
  .offer-card { position: absolute; left: 40px; width: 1120px; background: var(--card-bg); border-radius: 12px; display: flex; align-items: center; }
  .offer-icon { position: absolute; left: 46px; width: 220px; height: 220px; border-radius: 50%; background: var(--icon-bg);
    display: flex; align-items: center; justify-content: center; }
  .offer-mark { font-weight: 700; font-size: 54px; color: var(--navy); }
  .offer-text { margin-left: 334px; width: 750px; font-size: 38px; line-height: 57px; color: var(--body-text); }
  .card-software { top: 250px; height: 428px; }
  .card-risk { top: 702px; height: 318px; }
  .card-warranty { top: 1044px; height: 320px; }

  .footer { position: absolute; left: 0; top: 3404px; width: 1200px; height: 128px; background: var(--white); text-align: center;
    font-size: 28px; color: #222; line-height: 128px; }
</style>
</head>
<body>
  <header class="header">
    <div class="brand"><span class="brand-name">PELKO</span><span class="brand-sub">RADIANT</span></div>
    <div class="contact">
      <svg width="104" height="104" viewBox="0 0 24 24" fill="none" stroke="#1c2546" stroke-width="1.3" stroke-linecap="round" stroke-linejoin="round" aria-hidden="true">
        <path d="M22 16.9v3a2 2 0 0 1-2.2 2 19.8 19.8 0 0 1-8.6-3.1 19.5 19.5 0 0 1-6-6A19.8 19.8 0 0 1 2.1 4.2 2 2 0 0 1 4.1 2h3a2 2 0 0 1 2 1.7c.1.9.4 1.8.7 2.7a2 2 0 0 1-.5 2.1L8 9.8a16 16 0 0 0 6 6l1.3-1.3a2 2 0 0 1 2.1-.4c.9.3 1.8.6 2.7.7a2 2 0 0 1 1.7 2z"/>
        <path d="M15 5a5 5 0 0 1 4 4M15 1a9 9 0 0 1 8 8"/>
      </svg>
      <div><div class="contact-label">CALL US</div><div class="contact-number">(555) 318-4472</div></div>
    </div>
    <div class="sensor-visual" role="img" aria-label="Photo of the PELKO dental x-ray sensor with its cable"></div>
  </header>

  <section class="subscribe">
    <h2 class="section-title">SUBSCRIBE</h2>
    <div class="rule"></div>
    <div class="price price-one"><div class="price-amount">$1,999</div><span class="price-tag">ONE TIME FEE</span></div>
    <div class="price price-two"><div class="price-amount">$139</div><span class="price-tag">/ MONTH</span></div>
  </section>

  <section class="promo">
    <p class="promo-headline">50% off the sign up fee</p>
    <p class="promo-expiry">offer expires Dec 1<sup>st</sup> 2020</p>
  </section>

  <section class="offers">
    <h2 class="section-title">OUR OFFERS</h2>
    <div class="rule"></div>
    <div class="offer-card card-software">
      <div class="offer-icon"><span class="offer-mark">VANTA</span></div>
      <p class="offer-text">VANTA is GUARANTEED to work seamlessly in all major imaging software applications, including Morvex 9/10/11, Talden QRP, Brivolane, Quorin TelaPix, Novrida, Harbinview/Whitcombe Imaging, Stelvar Kobinex and more!</p>
    </div>
    <div class="offer-card card-risk">
      <div class="offer-icon" role="img" aria-label="Money-back icon"></div>
      <p class="offer-text">No Risk....try us worry free for 30 days or your money back!</p>
    </div>
    <div class="offer-card card-warranty">
      <div class="offer-icon" role="img" aria-label="Support agent illustration"></div>
      <p class="offer-text">Lifetime no-deductible warranty, support and software upgrades for PELKO Circle members</p>
    </div>
  </section>

  <footer class="footer">Copyright © 2020 All Rights Reserved</footer>
</body>
</html>
```